Website Design for new skincare product launch/rebranding

The Dew Harbor website is currently live and built through Pagelume.com. While the existing site has served as a strong starting point, I’m now looking to elevate the overall experience with a complete redesign that reflects the growth and vision of the brand. This will be a full visual and functional revamp — not just a refresh — with the goal of creating a more elevated, intuitive, and conversion-focused platform. I’m looking for a designer who can not only reimagine the layout and visuals, but also collaborate on optimizing the user journey and site structure for both storytelling and sales.

Target Market(s)

Age 25- 45 (core), with secondary appeal to 18-55. Primarily women, but gender inclusive. Wellness/Holistic Beauty/Organic Ingredients, Botanical.

Industry/Entity Type

Beauty, aesthetics, wellness.

Number of Pages Required

5+ page

Font styles to use
Other font styles liked:
• Thorvale Sans Family

Colors

Designer to choose colors to be used in the design.

Requirements
Must have
• Include standard pages (Home, Our Story/Values, Shop, Product Detail with ingredients/description/etc., Contact) and any other recommended sections to optimize conversion. Minimal, clean, calming visual. Seamlessly integrate with Vendara for all product sales.
Nice to have
• Company colors are attached in images, along with first two products that are launching. One called Lumivelt, and one called Serapoise. Fonts and shapes need to align accordingly. Feel elevated, neutral, and luxe while maintaining a grounded, earthy minimalism. Visual inspiration includes brands like Maple Tenet, Vessa Orlaine, and TOrveli — minimal yet high-end, with thoughtful use of whitespace, typography, and subtle movement. Would LOVE to have movement (short clip GIF) on either the home page or ingredient page, reference TOrveli website (homepage or LumaKnit Process™ Tab)
Should not have
• dark colors, complex design elements, too many different fonts. For ingredients, stick to botanical images and information only, with no mentions of CBD or use of leaf imagery.

```html
<!DOCTYPE html>
<html lang="en">
<head>
<meta charset="utf-8">
<title>Dew Harbor — Balanced Skincare</title>
<link href="https://fonts.googleapis.com/css2?family=Josefin+Sans:wght@400;600;700&family=Jost:ital,wght@0,300;0,400;0,500;1,300&family=Allura&display=swap" rel="stylesheet">
<style>
:root{
  --stone:#8f8e88;
  --stone-dark:#7c7a74;
  --taupe:#dacdc4;
  --taupe-line:#c7b8ae;
  --peach:#f8e4d7;
  --peach-soft:#fcefe6;
  --ink:#2f2d2b;
  --body:#4a4744;
  --muted:#a8a19b;
  --white:#ffffff;
}
*{box-sizing:border-box;margin:0;padding:0}
html,body{width:1200px;height:4515px;overflow:hidden}
body{position:relative;background:var(--white);font-family:"Jost",sans-serif;color:var(--body)}
.abs{position:absolute}
.script{font-family:"Allura",cursive;color:var(--ink);font-size:26px;line-height:1}
.title{font-family:"Josefin Sans",sans-serif;font-weight:700;color:var(--ink);letter-spacing:1.5px;text-transform:uppercase}
.center{left:0;width:1200px;text-align:center}
.btn{position:absolute;background:var(--taupe);color:var(--ink);font-family:"Josefin Sans",sans-serif;font-size:11px;letter-spacing:1.5px;text-transform:uppercase;display:flex;align-items:center;justify-content:center;box-shadow:4px 4px 0 -1px var(--white),4px 4px 0 0 var(--taupe-line)}
.btn.stone{background:var(--stone);color:var(--white)}
.band{position:absolute;left:0;width:1200px}
.photo{position:absolute}

/* top bar & header */
.topbar{top:0;height:24px;background:var(--stone);color:var(--white);font-size:11px;letter-spacing:1.2px;text-align:center;line-height:24px;font-family:"Josefin Sans",sans-serif}
.header{top:24px;height:78px;background:var(--white)}
.nav{position:absolute;left:100px;top:31px;display:flex;gap:31px;font-size:12px;color:var(--ink)}
.brand{position:absolute;left:500px;width:200px;top:28px;text-align:center;font-family:"Josefin Sans",sans-serif;font-size:18px;letter-spacing:2px;color:var(--muted);text-transform:uppercase}
.header-icons{position:absolute;left:1000px;top:51px;display:flex;gap:17px}

/* hero */
.hero{top:102px;height:522px;background:linear-gradient(120deg,#f9e6da 0%,#f8e2d4 55%,#fbeee5 56%,#f6d9c8 100%)}
.hero h1{position:absolute;left:100px;top:180px;font-size:42px;line-height:55px}
.hero p{position:absolute;left:100px;top:303px;font-size:12.5px;color:var(--ink)}

/* values */
.value{position:absolute;width:260px;text-align:center}
.value h3{font-family:"Josefin Sans",sans-serif;font-weight:400;font-size:18px;letter-spacing:1px;color:var(--ink);margin-top:12px}
.value p{font-size:12.5px;line-height:17px;margin-top:12px;color:var(--ink)}
.divider{position:absolute;width:1px;background:#cfc9c4;top:885px;height:122px}

/* featured */
.featured{top:1148px;height:945px;background:linear-gradient(160deg,#fdf0e8 0%,#f9e4d8 100%)}
.card{position:absolute;border:1px solid #cdbfb6;background:linear-gradient(180deg,#fbf2ec,#f6ebe4)}
.prod h4{font-family:"Josefin Sans",sans-serif;font-weight:700;font-size:16.5px;letter-spacing:1px;color:var(--ink)}
.prod .price{font-family:"Josefin Sans",sans-serif;font-weight:600;font-size:14px;color:var(--ink);margin-top:10px}
.prod .sub{font-size:12px;color:var(--muted);line-height:19px;margin-top:10px}
.prod .desc{font-size:11.5px;line-height:18px;color:var(--ink);margin-top:4px;width:390px}
.feat{display:flex;align-items:center;margin-top:8px;font-size:10.5px;color:var(--muted)}
.feat i{font-family:"Allura",cursive;font-style:normal;font-size:16px;color:var(--ink);width:112px}

/* ingredients */
.tile{position:absolute;width:131px;height:128px;background:var(--white);border-radius:6px;box-shadow:0 3px 10px rgba(120,100,90,.18);text-align:center;font-size:17px;color:#8b8782;font-weight:300}
.tile svg{display:block;margin:22px auto 14px}

/* reviews */
.reviews{top:2905px;height:424px;background:linear-gradient(180deg,#fbe9df,#fcefe7)}
.review{position:absolute;width:400px;text-align:center;top:3090px}
.stars{color:#9a948e;font-size:14px;letter-spacing:4px}
.quote{font-style:italic;font-weight:300;font-size:17px;line-height:27px;color:#6b6762;margin-top:8px}
.who{font-size:13px;color:#8f8a85;margin-top:6px}

/* join */
.join{top:3714px;height:461px;background:linear-gradient(120deg,#fbeee6,#f8e1d4)}

/* footer */
.footer{top:4175px;height:340px;background:var(--stone)}
.footer h5{font-family:"Josefin Sans",sans-serif;font-weight:600;font-size:12px;letter-spacing:1.2px;color:var(--white);text-transform:uppercase}
.footer .links a{display:block;color:var(--white);font-size:12px;text-decoration:none;line-height:27.5px}
.contact-row{position:absolute;left:545px;display:flex;gap:14px;align-items:flex-start;color:var(--white);font-size:12px;line-height:19px}
.icon-dot{width:24px;height:24px;border-radius:50%;background:var(--white);display:flex;align-items:center;justify-content:center;flex:none}
</style>
</head>
<body>

<div class="band topbar">FREE SHIPPING ON ORDER OVER $79</div>

<header class="band header">
  <nav class="nav"><span>Shop</span><span>Our Story</span><span>Ingredients</span><span>Journal</span><span>Contact</span></nav>
  <div class="brand">Dew Harbor</div>
  <div class="btn" style="left:834px;top:22px;width:147px;height:31px;font-size:10.5px">Shop Now</div>
  <div class="header-icons" style="top:26px">
    <svg width="20" height="20" viewBox="0 0 20 20" fill="none" stroke="#3a3836" stroke-width="1.5"><circle cx="8.5" cy="8.5" r="6"/><path d="M13 13l5 5"/></svg>
    <svg width="20" height="20" viewBox="0 0 20 20" fill="none" stroke="#3a3836" stroke-width="1.5"><circle cx="10" cy="6.5" r="4"/><path d="M3 19c0-4 3-6.5 7-6.5s7 2.5 7 6.5"/></svg>
    <svg width="20" height="20" viewBox="0 0 20 20" fill="none" stroke="#3a3836" stroke-width="1.5"><path d="M4 7h12l-1 11H5z"/><path d="M7 7V5a3 3 0 016 0v2"/></svg>
  </div>
</header>

<section class="band hero">
  <div class="script abs" style="left:100px;top:150px;font-size:24px">Welcome to Dew Harbor</div>
  <h1 class="title">Balanced Skincare<br>For Every Body</h1>
  <p>Elevated botanical formulations for hydrated, healthy, and naturally radiant skin.</p>
  <div class="btn stone" style="left:100px;top:348px;width:175px;height:34px">Shop Skincare</div>
  <div class="btn stone" style="left:287px;top:348px;width:175px;height:34px">Discover Our Story</div>
  <div class="photo" role="img" aria-label="Two white serum dropper bottles and two white balm jars" style="left:675px;top:91px;width:525px;height:431px;background:radial-gradient(ellipse at 55% 55%,#f1efee 0%,#e6e3e1 35%,rgba(246,224,212,0) 70%)"></div>
</section>

<section class="band" style="top:624px;height:524px">
  <div class="script abs center" style="top:70px;font-size:24px">Our Value</div>
  <h2 class="title abs center" style="top:104px;font-size:31px;line-height:40px">Skin Care That Works<br>With Your Skin, Not Against It</h2>
  <p class="abs center" style="top:190px;font-size:12.5px;line-height:20px;color:var(--ink)">Our formulations are designed to enhance your skin's natural balance,<br>combining the best of nature with proven science</p>
</section>
<div class="value" style="left:171px;top:884px">
  <svg width="44" height="44" viewBox="0 0 44 44" fill="#8f8e88"><circle cx="10" cy="8" r="3"/><circle cx="22" cy="5" r="3"/><circle cx="34" cy="8" r="3"/><path d="M2 22c5-4 8 4 13 0s8 4 13 0 8 4 14 0v20H2z"/></svg>
  <h3>HYDRATION FIRST</h3><p>Lock in moisture<br>without heaviness.</p>
</div>
<div class="divider" style="left:440px"></div>
<div class="value" style="left:441px;top:884px">
  <svg width="44" height="44" viewBox="0 0 44 44" fill="#8f8e88"><path d="M4 20h36c0 10-8 16-18 16S4 30 4 20z"/><rect x="14" y="36" width="16" height="4"/><path d="M26 18l10-14 3 2-9 12z"/></svg>
  <h3>EARTH-ALIGNED</h3><p>Botanical purity, backed<br>by science.</p>
</div>
<div class="divider" style="left:708px"></div>
<div class="value" style="left:742px;top:884px">
  <svg width="44" height="44" viewBox="0 0 44 44" fill="none" stroke="#8f8e88" stroke-width="5"><path d="M16 10l6-6 6 6M8 32l-4-8 8-4M36 32l4-8-8-4"/><path d="M14 38h16"/></svg>
  <h3>SUSTAINABLE CHOICES</h3><p>Packaging you can feel<br>good about.</p>
</div>
<div class="btn" style="left:505px;top:1034px;width:187px;height:35px">View Our Story</div>

<section class="band featured">
  <div class="script abs center" style="top:72px;font-size:24px">Skincare Product</div>
  <h2 class="title abs center" style="top:106px;font-size:31px">Featured Products</h2>
</section>
<div class="card" style="left:140px;top:1310px;width:491px;height:342px">
  <div role="img" aria-label="Two frosted serum dropper bottles" style="position:absolute;left:120px;top:20px;width:250px;height:300px;background:radial-gradient(ellipse at center,#dedcdb 0%,#eceae8 45%,rgba(246,235,228,0) 72%)"></div>
</div>
<div class="prod abs" style="left:662px;top:1326px">
  <h4>LUMIVELT</h4><div class="price">$56.36</div>
  <div class="sub">Advanced hydration with weightless clarity<br>Deep Hydration Meets Botanical Calm</div>
  <div class="desc">A lightweight yet deeply hydrating moisturizer formulated with cucumber extract and hyaluronic acid to calm, cool, and plump your skin. Perfect for sensitive and combination types, it locks in lasting moisture without feeling heavy.</div>
  <div class="feat" style="margin-top:14px"><i>Hydration First -</i>Intensely moisturizes without clogging pores</div>
  <div class="feat"><i>Botanical Science -</i>Powered by cucumber, aloe, and chamomile</div>
  <div class="feat"><i>Sustainable Beauty -</i>100% recyclable packaging</div>
</div>
<div class="btn" style="left:662px;top:1594px;width:147px;height:36px">Learn More</div>

<div class="prod abs" style="left:140px;top:1699px">
  <h4>SERAPOISE</h4><div class="price">$56.36</div>
  <div class="sub">Advanced hydration with weightless clarity<br>Deep Hydration Meets Botanical Calm</div>
  <div class="desc">A lightweight yet deeply hydrating moisturizer formulated with cucumber extract and hyaluronic acid to calm, cool, and plump your skin. Perfect for sensitive and combination types, it locks in lasting moisture without feeling heavy.</div>
  <div class="feat" style="margin-top:14px"><i>Hydration First -</i>Intensely moisturizes without clogging pores</div>
  <div class="feat"><i>Botanical Science -</i>Powered by cucumber, aloe, and chamomile</div>
  <div class="feat"><i>Sustainable Beauty -</i>100% recyclable packaging</div>
</div>
<div class="btn" style="left:140px;top:1969px;width:149px;height:34px">Learn More</div>
<div class="card" style="left:569px;top:1685px;width:491px;height:342px">
  <div role="img" aria-label="Two white botanical balm sticks" style="position:absolute;left:120px;top:40px;width:250px;height:260px;background:radial-gradient(ellipse at center,#ecebea 0%,#f3f0ee 45%,rgba(246,235,228,0) 72%)"></div>
</div>

<section class="band" style="top:2093px;height:812px">
  <div class="script abs center" style="top:110px;font-size:24px">Wellness in Every Drop</div>
  <h2 class="title abs center" style="top:143px;font-size:31px;line-height:42px">Ingredients You<br>Can Feel Good About</h2>
  <p class="abs center" style="top:230px;font-size:12px;line-height:18.5px;color:var(--ink)">Our botanicals aren't just beautiful — they're clinically chosen to nourish, protect, and renew your skin.<br>Powerful plant actives, guided by science, to help your skin glow naturally. Nature's wisdom, enhanced by<br>modern formulation for skin that thrives.</p>
</section>
<div class="btn" style="left:505px;top:2400px;width:187px;height:34px">See All Ingredients</div>

<div class="tile" style="left:287px;top:2458px"><svg width="44" height="44" viewBox="0 0 44 44"><circle cx="22" cy="22" r="17" fill="#9c9994"/><circle cx="22" cy="22" r="11" fill="#d4d1cd"/></svg>Cucumber</div>
<div class="tile" style="left:131px;top:2528px"><svg width="44" height="44" viewBox="0 0 44 44" fill="#9c9994"><path d="M16 6h12v4l-2 2v8l10 16H6l10-16v-8l-2-2z"/></svg>Aloe Vera</div>
<div class="tile" style="left:445px;top:2528px"><svg width="44" height="44" viewBox="0 0 44 44" fill="#9c9994"><circle cx="22" cy="22" r="6"/><circle cx="22" cy="8" r="5"/><circle cx="22" cy="36" r="5"/><circle cx="8" cy="22" r="5"/><circle cx="36" cy="22" r="5"/><circle cx="12" cy="12" r="5"/><circle cx="32" cy="32" r="5"/><circle cx="32" cy="12" r="5"/><circle cx="12" cy="32" r="5"/></svg>Chamomile</div>
<div class="tile" style="left:287px;top:2612px"><svg width="44" height="44" viewBox="0 0 44 44" fill="#9c9994"><circle cx="16" cy="28" r="9"/><circle cx="30" cy="16" r="7"/><circle cx="32" cy="32" r="5"/></svg>Rosehip Oil</div>
<div class="tile" style="left:131px;top:2682px"><svg width="44" height="44" viewBox="0 0 44 44" fill="#9c9994"><circle cx="10" cy="8" r="3"/><circle cx="22" cy="5" r="3"/><circle cx="34" cy="8" r="3"/><path d="M2 22c5-4 8 4 13 0s8 4 13 0 8 4 14 0v20H2z"/></svg>Cucumber</div>
<div class="tile" style="left:445px;top:2682px"><svg width="44" height="44" viewBox="0 0 44 44" fill="none" stroke="#9c9994" stroke-width="4"><path d="M22 40V18M22 18c0-8 6-12 12-12M22 24c-4-6-10-8-14-6"/></svg>Green Tea</div>

<div class="photo" style="left:646px;top:2587px;width:452px;height:228px;border-radius:14px;background:linear-gradient(135deg,#fdeee6,#f6d6c6)"></div>
<div class="photo" role="img" aria-label="Smiling woman holding cucumber slices near her eyes" style="left:790px;top:2400px;width:230px;height:415px;background:linear-gradient(180deg,rgba(222,212,206,.6) 0%,#e7b99c 40%,#d9a184 100%);border-radius:0 0 6px 6px"></div>

<section class="band reviews">
  <div class="script abs center" style="top:78px;font-size:24px">Customer Stories</div>
  <h2 class="title abs center" style="top:111px;font-size:31px">Social Proof &amp; Real Results</h2>
  <div class="abs" style="left:543px;top:349px;display:flex;gap:8px">
    <span style="width:20px;height:3px;background:#d8d2cd"></span><span style="width:28px;height:4px;background:#8f8e88"></span><span style="width:20px;height:3px;background:#d8d2cd"></span><span style="width:20px;height:3px;background:#d8d2cd"></span>
  </div>
</section>
<div class="review" style="left:80px"><div class="stars">★★★★★</div><div class="quote">The first product that made my skin<br>feel hydrated and calm without feeling heavy.<br>Deep Hydration Meets Botanical Calm</div><div class="who">Mara T., Verified Customer</div></div>
<div class="review" style="left:473px"><div class="stars">★★★★★</div><div class="quote">The first product that made my skin<br>feel hydrated and calm without feeling heavy.<br>Deep Hydration Meets Botanical Calm</div><div class="who">Mara T., Verified Customer</div></div>
<div class="review" style="left:865px"><div class="stars">★★★★★</div><div class="quote">The first product that made my skin<br>feel hydrated and calm without feeling heavy.<br>Deep Hydration Meets Botanical Calm</div><div class="who">Mara T., Verified Customer</div></div>

<section class="band" style="top:3329px;height:385px">
  <div class="script abs center" style="top:66px;font-size:30px">@ Follow On Pictora</div>
  <div class="photo" role="img" aria-label="Heron wading among reeds" style="left:100px;top:122px;width:187px;height:188px;background:linear-gradient(180deg,#6f6a55,#4a4636)"></div>
  <div class="photo" role="img" aria-label="Pier bridge at dusk over water" style="left:303px;top:122px;width:187px;height:188px;background:linear-gradient(180deg,#d6a4b2,#7a4a4e)"></div>
  <div class="photo" style="left:506px;top:122px;width:187px;height:188px;background:linear-gradient(200deg,#7b4fd6,#d24a8a 55%,#f08a3c)"></div>
  <div class="photo" role="img" aria-label="Smiling older woman on a phone in a forest" style="left:710px;top:122px;width:187px;height:188px;background:linear-gradient(180deg,#5d5a4c,#8c7d70)"></div>
  <div class="photo" role="img" aria-label="Seaside terrace lounge at sunset" style="left:913px;top:122px;width:187px;height:188px;background:linear-gradient(180deg,#d9c8c6,#8fa6b4 55%,#c9b7a6)"></div>
</section>

<section class="band join">
  <div class="script abs" style="left:191px;top:100px;font-size:24px">Join With Us</div>
  <h2 class="title abs" style="left:191px;top:133px;font-size:33px;line-height:42px">Join The Dew Harbor<br>Collective</h2>
  <p class="abs" style="left:191px;top:222px;font-size:21px;font-style:italic;font-weight:300;color:var(--ink)">Early access to launches + skincare insights.</p>
  <p class="abs" style="left:191px;top:259px;font-size:12px;line-height:18px;color:var(--ink)">Early access to product launches, expert skincare insights,<br>and exclusive offers—delivered with love, not spam.</p>
  <div class="btn stone" style="left:191px;top:314px;width:189px;height:35px">Join Us Now</div>
  <div class="photo" role="img" aria-label="Two white balm jars beside two serum dropper bottles" style="left:700px;top:79px;width:440px;height:382px;background:radial-gradient(ellipse at 55% 60%,#efedec 0%,#e6e3e1 35%,rgba(248,225,212,0) 70%)"></div>
</section>

<footer class="band footer">
  <div class="abs" style="left:100px;top:100px;width:215px;text-align:center;font-family:'Josefin Sans',sans-serif;font-size:24px;letter-spacing:2px;color:var(--white);text-transform:uppercase">Dew Harbor</div>
  <div class="abs" style="left:101px;top:196px;width:36px;height:36px;border-radius:50%;background:var(--white)"></div>
  <div class="abs" style="left:148px;top:196px;width:36px;height:36px;border-radius:50%;background:var(--white)"></div>

  <h5 class="abs" style="left:387px;top:86px">Quick Links</h5>
  <div class="links abs" style="left:387px;top:104px"><a>Shop Our</a><a>Story</a><a>Ingredients</a><a>Journal</a><a>Contact</a></div>

  <h5 class="abs" style="left:545px;top:86px">Contact Info</h5>
  <div class="contact-row" style="top:116px"><span class="icon-dot"><svg width="12" height="12" viewBox="0 0 12 12" fill="#8f8e88"><path d="M2 1l2 0 1 3-1.5 1a7 7 0 003.5 3.5L8 7l3 1v2a1 1 0 01-1 1A9 9 0 011 2a1 1 0 011-1z"/></svg></span><span style="padding-top:3px">555-014-2260</span></div>
  <div class="contact-row" style="top:154px"><span class="icon-dot"><svg width="12" height="10" viewBox="0 0 12 10" fill="none" stroke="#8f8e88" stroke-width="1.3"><rect x="1" y="1" width="10" height="8"/><path d="M1 1l5 4 5-4"/></svg></span><span style="padding-top:3px">hello@dewharbor.com</span></div>
  <div class="contact-row" style="top:190px"><span class="icon-dot"><svg width="10" height="13" viewBox="0 0 10 13" fill="#8f8e88"><path d="M5 0a5 5 0 015 5c0 4-5 8-5 8S0 9 0 5a5 5 0 015-5z"/><circle cx="5" cy="5" r="2" fill="#fff"/></svg></span><span>48 Tidewater Lane, Suite 12<br>Harbor Point</span></div>

  <h5 class="abs" style="left:846px;top:86px">Subscribe Newsletter</h5>
  <div class="abs" style="left:846px;top:117px;width:254px;height:35px;background:var(--white);font-size:10px;color:#b3aea9;padding:12px 16px">Email</div>
  <div class="btn" style="left:846px;top:166px;width:250px;height:35px;font-size:10.5px">Subscribe</div>

  <div class="abs" style="left:0;top:284px;width:1200px;height:1px;background:rgba(255,255,255,.45)"></div>
  <div class="abs center" style="top:307px;font-size:11px;color:var(--white);letter-spacing:.5px">© Copyright All Right Reserved 2025</div>
</footer>

</body>
</html>
```